VaultMeridan Business Card Re-Design

VaultMeridan is a specialized information security company that applies its proven methodology of security Assessment, Development, Integration and Training (A-D-I-T) to provide cyber security services in the areas of Data Protection, Network Defense and Compliance. We need the current business card re-designed to properly scale the fonts and possibly rearranging some elements (icons, lettering, etc.) to make the card more appealing to the eye. The card should have the logo that is on the web site (www.vaultmeridan-example.com). We would like ideas for both a black card (black background) and a white card (white background). We prefer rounded corners to help the card stand out but are open to all ideas. FYI: VaultMeridan's slogan is "...your security is our business".

Target Market(s)

#1 US Government Contracting Companies, #2 Commercial Companies, #3 Gen. Public.

Industry/Entity Type

Business

Contact Information for Business Card

See Description; open to the use of different fonts.

Font styles to use
Sans Serif

Colors
000000
ec1f27
ffffff

Requirements
Must have
• Company logo on web site, rounded corners, list of company offerings on the back of the card.
Nice to have
• Icons
Should not have
• none

```html
<!DOCTYPE html>
<html lang="en">
<head>
<meta charset="utf-8">
<title>VaultMeridan Business Card</title>
<link href="https://fonts.googleapis.com/css2?family=Open+Sans:wght@400;700&display=swap" rel="stylesheet">
<style>
  :root {
    --page: #e7e4df;
    --card: #262626;
    --card-deep: #1b1b1b;
    --red: #ec1f27;
    --white: #ffffff;
    --ink: #f2f2f2;
  }
  * { margin: 0; padding: 0; box-sizing: border-box; }
  html, body { width: 1200px; height: 1000px; overflow: hidden; }
  body {
    background: var(--page);
    font-family: "Open Sans", Arial, sans-serif;
    color: var(--ink);
    position: relative;
  }
  .card {
    position: absolute;
    left: 266px;
    width: 664px;
    height: 396px;
    background: var(--card);
    border-radius: 28px;
  }
  .card--front { top: 73px; }
  .card--back { top: 532px; }

  .brand {
    position: absolute;
    display: flex;
    align-items: center;
    gap: 12px;
  }
  .brand__dot {
    width: 18px; height: 18px;
    border-radius: 50%;
    background: var(--red);
  }
  .brand__name {
    font-weight: 400;
    font-size: 36px;
    letter-spacing: 2px;
    color: var(--white);
    line-height: 1;
  }
  .card--front .brand { right: 34px; top: 42px; }
  .brand-tagline {
    position: absolute;
    right: 58px; top: 100px;
    font-size: 17px;
    letter-spacing: 1.5px;
    color: var(--ink);
  }
  .card--back .brand { left: 32px; top: 34px; }

  .accent-bar {
    position: absolute;
    left: -2px; top: 127px;
    width: 10px; height: 62px;
    background: var(--red);
    border-radius: 0 4px 4px 0;
  }
  .contact {
    position: absolute;
    left: 32px; top: 122px;
    font-size: 16.5px;
    line-height: 21.5px;
  }
  .contact__name {
    font-weight: 700;
    font-size: 23px;
    line-height: 30px;
    color: var(--red);
  }
  .contact__role { margin-bottom: 9px; }
  .contact__address { margin-bottom: 10px; }
  .contact__list { list-style: none; }
  .contact__list li {
    display: flex;
    align-items: center;
    gap: 8px;
    height: 23.3px;
  }
  .contact__list svg { width: 13px; height: 13px; fill: var(--red); flex: none; }

  .mark-space {
    position: absolute;
    border-radius: 50%;
  }
  .card--front .mark-space {
    left: 384px; top: 150px;
    width: 200px; height: 200px;
    background: var(--card-deep);
  }
  .card--back .mark-space {
    left: 390px; top: 96px;
    width: 200px; height: 200px;
    background: var(--white);
  }

  .services {
    position: absolute;
    left: 30px; top: 105px;
    list-style: none;
    font-size: 16.6px;
    line-height: 20.3px;
  }
  .services li::before {
    content: "\2022";
    color: var(--red);
    margin-right: 5px;
  }
</style>
</head>
<body>

<section class="card card--front">
  <div class="brand">
    <span class="brand__dot"></span>
    <span class="brand__name">VaultMeridan</span>
  </div>
  <div class="brand-tagline">INFORMATION SECURITY</div>

  <div class="accent-bar"></div>
  <div class="contact">
    <div class="contact__name">Dorian Hale</div>
    <div class="contact__role">MSc, BSEE<br>President / CEO</div>
    <div class="contact__address">4410 Harrow Ln. Suite 210<br>Linthicum, Maryland 21090</div>
    <ul class="contact__list">
      <li><svg viewBox="0 0 14 14"><path d="M4 0h6a1 1 0 0 1 1 1v12a1 1 0 0 1-1 1H4a1 1 0 0 1-1-1V1a1 1 0 0 1 1-1zm0.5 1.5v9h5v-9z"/></svg>555.014.2290</li>
      <li><svg viewBox="0 0 14 14"><path d="M1 5c0-2 3-3 6-3s6 1 6 3v1h-3V4.5H4V6H1zM3 7h8l2 6H1z"/></svg>555.018.7734</li>
      <li><svg viewBox="0 0 14 14"><path d="M0 3h14v1L7 8 0 4zm0 2.5 7 4 7-4V11H0z"/></svg>info@vaultmeridan-example.com</li>
      <li><svg viewBox="0 0 14 14"><path d="M0 3h14v1L7 8 0 4zm0 2.5 7 4 7-4V11H0z"/></svg>dhale@vaultmeridan-example.com</li>
      <li><svg viewBox="0 0 14 14"><path d="M7 0a7 7 0 1 0 0 14A7 7 0 0 0 7 0zm0 1.5c.8 0 1.8 2 2 4.5H5c.2-2.5 1.2-4.5 2-4.5zM1.6 7.5h2.4c.1 1.8.5 3.4 1.1 4.4A5.5 5.5 0 0 1 1.6 7.5zm4.4 0h2c-.2 2.3-.7 4.5-1 4.5s-.8-2.2-1-4.5zm4 0h2.4a5.5 5.5 0 0 1-3.5 4.4c.6-1 1-2.6 1.1-4.4zM1.6 6A5.5 5.5 0 0 1 5.1 2.1C4.5 3 4.1 4.4 4 6zm8.4 0c-.1-1.6-.5-3-1.1-3.9A5.5 5.5 0 0 1 12.4 6z"/></svg>www.vaultmeridan-example.com</li>
    </ul>
  </div>

  <div class="mark-space" role="img" aria-label="Space for the VaultMeridan brand symbol, embossed in black"></div>
</section>

<section class="card card--back">
  <div class="brand">
    <span class="brand__dot"></span>
    <span class="brand__name">VaultMeridan</span>
  </div>

  <ul class="services">
    <li>Secure Cloud &amp; Open Source Solutions</li>
    <li>Network Attack Penetration &amp; Defense</li>
    <li>Red/Blue Team</li>
    <li>Data Center Consolidation</li>
    <li>Secure Virtual Computing</li>
    <li>Classified Cross Domian Solutions</li>
    <li>Foreign/Counter Intelligence Date Security</li>
    <li>Certification &amp; Accreditation</li>
    <li>Secure Wireless Solutions</li>
    <li>Security Training , Assessments &amp; Integration</li>
    <li>Security Subject Matter Experts</li>
    <li>Executive Security Strategy Coaching</li>
    <li>Data Encryption/Privacy</li>
  </ul>

  <div class="mark-space" role="img" aria-label="Space for the VaultMeridan brand symbol in white and red"></div>
</section>

</body>
</html>
```